Bref créative
Corvane Oral Care Stationary
Corvane Oral Care
Professional
R. Lucien Dorvash, DDS, MAGD
2483 W Perrin Ave.
Larkfield, TX 77841
dentist@qbl.zx.com
www.corvaneoralcare.com

```html
<!DOCTYPE html>
<html lang="en">
<head>
<meta charset="utf-8">
<title>Corvane Oral Care Stationery</title>
<link href="https://fonts.googleapis.com/css2?family=Open+Sans:wght@400;600;700&display=swap" rel="stylesheet">
<style>
:root{
  --bg:#e9e9e7;
  --paper:#ffffff;
  --teal:#1f86a8;
  --teal-deep:#156a88;
  --mint:#acd6a4;
  --mint-soft:#d8ecd2;
  --ink:#24406a;
  --muted:#5b6570;
  --dark:#1e262c;
  --shadow:0 3px 8px rgba(0,0,0,.25);
}
*{margin:0;padding:0;box-sizing:border-box}
html,body{width:1200px;height:794px;overflow:hidden}
body{background:var(--bg);font-family:"Open Sans",Arial,sans-serif;color:var(--ink);position:relative}
.piece{position:absolute;box-shadow:var(--shadow);overflow:hidden}

/* brand lockup */
.brand{display:flex;align-items:center;gap:5px;color:var(--ink);font-weight:700;white-space:nowrap}
.brand-dot{border-radius:50%;background:var(--teal);flex:none}
.brand.on-dark{color:#fff}
.brand.on-dark .brand-dot{background:var(--mint)}

/* business cards */
.card{left:84px;width:187px;border-radius:9px;background:var(--paper)}
.card-front{top:108px;height:120px}
.card-front .band{position:absolute;left:0;top:0;width:100%;height:26px;background:linear-gradient(90deg,var(--paper) 0%,var(--mint-soft) 35%,var(--teal) 100%)}
.card-front .name{position:absolute;left:66px;top:4px;font-size:8px;font-weight:700;color:var(--dark)}
.card-front .title{position:absolute;left:84px;top:15px;font-size:5px;color:var(--dark)}
.card-front .brand{position:absolute;left:8px;top:38px;font-size:7px;flex-direction:column;align-items:flex-start;gap:3px;width:58px;white-space:normal;line-height:1.1}
.card-front .brand-dot{width:20px;height:20px}
.card-front .details{position:absolute;left:78px;top:36px;font-size:5px;line-height:1.7;color:var(--muted)}
.card-front .wave{position:absolute;left:0;bottom:0;width:100%;height:18px}

.card-back{display:flex;flex-direction:column;align-items:center;justify-content:center;gap:4px}
.card-back .brand{font-size:10px}
.card-back .brand-dot{width:18px;height:18px}
.card-back .web{font-size:5px;color:var(--muted)}
.card-white{top:252px;height:108px;background:var(--paper)}
.card-mint{top:391px;height:113px;background:var(--mint)}
.card-dark{top:533px;height:110px;background:var(--dark)}
.card-dark .web{color:#c9d3d8}

/* letterhead */
.letterhead{left:293px;top:108px;width:372px;height:547px;background:var(--paper)}
.letterhead .band{position:absolute;right:0;top:0;width:78%;height:26px;background:linear-gradient(90deg,var(--paper) 0%,var(--mint-soft) 30%,var(--mint) 65%,var(--teal) 100%);clip-path:polygon(0 0,100% 0,100% 100%,8% 100%)}
.letterhead .brand{position:absolute;left:22px;top:40px;font-size:11px;flex-direction:column;align-items:flex-start;gap:4px}
.letterhead .brand-dot{width:30px;height:30px}
.letterhead .footer{position:absolute;left:0;right:0;bottom:14px;text-align:center;font-size:5.5px;line-height:1.6;color:var(--muted)}
.letterhead .footer span{margin:0 6px}
.letterhead .rule{position:absolute;left:20px;right:20px;bottom:8px;height:2px;background:var(--teal)}

/* envelope backs */
.env-back{left:715px;width:413px;height:101px;box-shadow:none;overflow:visible}
.env-back svg{display:block;width:100%;height:100%;filter:drop-shadow(0 2px 3px rgba(0,0,0,.25))}
.env-back .brand{position:absolute;left:50%;top:38px;transform:translateX(-50%);font-size:10px}
.env-back .brand-dot{width:16px;height:16px}
.env-white{top:108px}
.env-black{top:182px}
.env-mint{top:256px}

/* envelope front */
.env-front{left:715px;top:533px;width:413px;height:127px;background:var(--paper)}
.env-front .band{position:absolute;left:0;top:0;width:100%;height:20px;background:linear-gradient(90deg,var(--teal) 0%,var(--mint) 55%,var(--mint-soft) 100%)}
.env-front .brand{position:absolute;left:14px;top:28px;font-size:10px;flex-direction:column;align-items:flex-start;gap:3px}
.env-front .brand-dot{width:24px;height:24px}
.env-front .return{position:absolute;left:14px;bottom:8px;font-size:6px;color:var(--muted)}
</style>
</head>
<body>

<!-- Business card: contact side -->
<div class="piece card card-front">
  <div class="band"></div>
  <div class="name">R. Lucien Dorvash</div>
  <div class="title">DDS, MAGD</div>
  <div class="brand"><span class="brand-dot"></span>Corvane Oral Care</div>
  <div class="details">
    2483 W Perrin Ave., Larkfield, TX 77841<br>
    281-555-0148<br>
    281-555-0192<br>
    dentist@qbl.zx.com<br>
    www.corvaneoralcare.com
  </div>
  <svg class="wave" viewBox="0 0 187 18" preserveAspectRatio="none">
    <path d="M0 10 Q60 0 120 8 T187 4 V18 H0Z" fill="var(--teal)"/>
    <path d="M0 14 Q70 6 130 12 T187 9 V18 H0Z" fill="var(--teal-deep)"/>
  </svg>
</div>

<!-- Business card backs -->
<div class="piece card card-back card-white">
  <div class="brand"><span class="brand-dot"></span>Corvane Oral Care</div>
  <div class="web">www.corvaneoralcare.com</div>
</div>
<div class="piece card card-back card-mint">
  <div class="brand"><span class="brand-dot"></span>Corvane Oral Care</div>
  <div class="web">www.corvaneoralcare.com</div>
</div>
<div class="piece card card-back card-dark">
  <div class="brand on-dark"><span class="brand-dot"></span>Corvane Oral Care</div>
  <div class="web">www.corvaneoralcare.com</div>
</div>

<!-- Letterhead -->
<div class="piece letterhead">
  <div class="band"></div>
  <div class="brand"><span class="brand-dot"></span>Corvane Oral Care</div>
  <div class="footer">
    2483 W Perrin Ave., Larkfield, TX 77841<br>
    <span>281-555-0148</span><span>dentist@qbl.zx.com</span><br>
    www.corvaneoralcare.com
  </div>
  <div class="rule"></div>
</div>

<!-- Envelope backs -->
<div class="piece env-back env-white">
  <svg viewBox="0 0 413 101" preserveAspectRatio="none">
    <rect x="0" y="0" width="413" height="101" fill="#f4f4f4"/>
    <path d="M0 0 H413 V20 L236 98 Q206 108 176 98 L0 20Z" fill="var(--paper)"/>
  </svg>
  <div class="brand"><span class="brand-dot"></span>Corvane Oral Care</div>
</div>
<div class="piece env-back env-black">
  <svg viewBox="0 0 413 101" preserveAspectRatio="none">
    <path d="M0 0 H413 V20 L236 98 Q206 108 176 98 L0 20Z" fill="var(--dark)"/>
  </svg>
  <div class="brand on-dark"><span class="brand-dot"></span>Corvane Oral Care</div>
</div>
<div class="piece env-back env-mint">
  <svg viewBox="0 0 413 101" preserveAspectRatio="none">
    <path d="M0 0 H413 V20 L236 98 Q206 108 176 98 L0 20Z" fill="var(--mint)"/>
  </svg>
  <div class="brand"><span class="brand-dot"></span>Corvane Oral Care</div>
</div>

<!-- Envelope front -->
<div class="piece env-front">
  <div class="band"></div>
  <div class="brand"><span class="brand-dot"></span>Corvane Oral Care</div>
  <div class="return">2483 W Perrin Ave., Larkfield, TX 77841</div>
</div>

</body>
</html>
```